Corvane Networks web design

Corvane is an Internet Service Provider bringing high-speed service to homes and businesses. Our principal market target is rural areas of West Michigan, but we intend to expand rapidly. We need a website to market our services, facilitate online ordering, customer support and communicate with our customers.

I will upload a draft outline of the content we hope to include in the website.

We compete directly with Halberd Communications, Lumetra, Dravix and Kelwick communications to bring Internet service to homes and businesses in our coverage area.

Our primary values include:

1. Unlike our competitors, we do not require long term contractors or service bundles; There are no termination fees, for example. All services are sold on a recurring 1-month agreement term.
2. Unlike other wireless (mobile) providers, we do not limit downloads or uploads with bit/byte buckets
3. We provide service to areas ignored by the larger carriers - Rural areas in Michigan that lack options for broadband are prime targets for Corvane to cover.
4. Unlike other wireless ISP's, we utilize licensed FCC spectrum. We do not use unlicensed/free frequencies, providing us an advantage for reliability and stability.
Updates

So many wonderful designs, thank you very much for all your hard work. We are evaluating all our favorite designs and plan to make a selection in the next 2 days. I will be in touch with you to request revisions if necessary or further refinements.  Thank you again for your efforts on this project.

Target Market(s)

Our target market is home Internet users. however, that does not mean that our users are "high tech" oriented - they are just normal mom's and pop's who buy Internet for home use. The site should be easy to navigate and communicate our message of speed, value, reliability and facilitate simple product ordering.

Industry/Entity Type

Internet

Requirements
Must have
• Our phone number should be prominently displayed 1-844-7NU-LINK
• Our logo is uploaded in the attachments.
• Design for desktop and mobile devices.
Nice to have
• The most modern of web design trends. Such as a design that facilitates parallax scrolling effects rather than lots of individual pages.
• Stock artwork communicating our values of speed and reliability.

```html
<!DOCTYPE html>
<html lang="en">
<head>
<meta charset="utf-8">
<title>Corvane Networks</title>
<link href="https://fonts.googleapis.com/css2?family=Open+Sans:wght@400;600;700&display=swap" rel="stylesheet">
<style>
:root{
  --orange:#f7880f;
  --orange-dark:#e27100;
  --black:#050505;
  --ink:#222;
  --body:#5a5a5a;
  --grey-band:#d9d9dc;
  --sky:#14a9e6;
  --link:#2a9bd6;
  --red-link:#d9481a;
  --footer:#363636;
  --footer-base:#2b2b2b;
  --white:#fff;
}
*{margin:0;padding:0;box-sizing:border-box}
html,body{width:711px;height:1200px;overflow:hidden}
body{position:relative;font-family:"Open Sans",Arial,sans-serif;color:var(--ink);background:var(--white)}
.abs{position:absolute}

/* header */
.site-header{left:0;top:0;width:711px;height:67px;background:var(--black)}
.brand{left:58px;top:18px;font-size:24px;font-weight:700;color:var(--orange);letter-spacing:1px}
.hotline{left:412px;top:23px;font-size:13px;font-weight:700;color:var(--orange);display:flex;align-items:center;gap:6px}
.account{left:569px;top:9px;font-size:7.5px;color:#ddd;word-spacing:4px}
.social-dots{left:567px;top:30px;display:flex;gap:8px}
.social-dots span{width:20px;height:20px;border-radius:50%;background:radial-gradient(#f2f2f2,#9a9a9a)}

/* nav */
.main-nav{left:0;top:67px;width:711px;height:28px;background:linear-gradient(#fff,#ececec);border-bottom:1px solid #d4d4d4;display:flex;padding-left:58px}
.main-nav a{font-size:8.5px;color:#222;text-decoration:none;padding:0 16px;line-height:27px;border-right:1px solid #ddd}
.main-nav a.active{background:var(--orange);color:#fff}

/* hero */
.hero-band{left:0;top:95px;width:711px;height:241px;background:var(--grey-band)}
.slider{left:58px;top:107px;width:588px;height:229px;background:linear-gradient(90deg,#a9a9ad,#c4c4c8 45%,#d2d2d5);border:1px solid #fff;overflow:hidden}
.slider-photo{right:0;top:0;width:300px;height:229px;
  background:
    radial-gradient(ellipse 70px 90px at 225px 150px,rgba(200,222,226,.95),rgba(200,222,226,0) 100%),
    radial-gradient(ellipse 28px 34px at 195px 70px,rgba(196,146,112,.85),rgba(196,146,112,0) 100%),
    radial-gradient(ellipse 70px 55px at 60px 105px,rgba(70,78,92,.85),rgba(70,78,92,0) 100%),
    radial-gradient(ellipse 90px 40px at 120px 200px,rgba(60,62,70,.6),rgba(60,62,70,0) 100%),
    radial-gradient(ellipse 120px 70px at 70px 20px,rgba(250,252,246,1),rgba(250,252,246,0) 100%),
    linear-gradient(160deg,#eef0ea 0%,#d9dcd8 35%,#b9bcc0 65%,#8f939a 100%);
  mask-image:linear-gradient(90deg,transparent 0,#000 18px)}
.slider-arrow{left:17px;top:133px;width:17px;height:17px;border-radius:50%;background:#e4e4e6}
.hero-title{left:0;width:215px;top:48px;text-align:right;color:#fff;font-size:13.5px;font-weight:600;line-height:28px}
.hero-points{left:0;width:215px;top:120px;text-align:right;color:#fff;font-size:10.5px;font-weight:600;line-height:28.5px}
.hero-points li{list-style:none;display:flex;justify-content:flex-end;align-items:center;gap:5px}
.hero-shadow{left:150px;top:336px;width:430px;height:14px;background:radial-gradient(ellipse at top,rgba(0,0,0,.22),transparent 70%)}

/* services */
.section-title{font-size:14px;font-weight:400;color:var(--ink)}
.section-title em{font-style:normal;color:var(--orange)}
.services-title{left:59px;top:352px}
.service-card{top:381px;width:175px;height:94px;overflow:hidden}
.service-card .photo{width:100%;height:100%}
.service-card .caption{position:absolute;left:0;bottom:0;width:100%;height:18px;background:rgba(40,40,40,.7);color:#fff;font-size:10px;font-weight:600;line-height:18px;padding-left:7px}
.card-home{left:59px}.card-home .photo{background:linear-gradient(135deg,#c9a37a,#6d4e33)}
.card-business{left:267px}.card-business .photo{background:linear-gradient(135deg,#f1f1f1,#8d8d8d 60%,#2d2d2d)}
.card-coverage{left:472px;background:#a7a6b3}
.card-coverage .photo{background:linear-gradient(160deg,#b9b8c4,#9897a6)}
.address-field{left:27px;top:52px;width:134px;height:17px;background:#fff;border:1px solid #ddd;font-size:6px;font-style:italic;color:#999;line-height:15px;padding-left:8px}
.check-btn{position:absolute;right:8px;bottom:2px;background:var(--orange);color:#fff;font-size:7px;font-weight:600;padding:2px 9px;line-height:10px}

/* welcome */
.welcome-title{left:0;top:511px;width:711px;text-align:center;font-size:14px}
.rule{left:58px;top:536px;width:589px;border-top:1px dotted #c0392b}
.welcome-text{left:58px;top:549px;width:589px;font-size:7.2px;line-height:12px;color:var(--body)}
.more-btn{left:305px;top:623px;width:48px;height:17px;background:var(--orange);border:1px solid #fbb669;color:#fff;font-size:7.5px;text-align:center;line-height:15px}

/* columns */
.col-head{top:671px;width:177px;height:25px;color:#fff;font-size:12.5px;font-weight:400;line-height:25px;padding-left:14px;box-shadow:0 1px 3px rgba(0,0,0,.25)}
.head-news{left:58px;background:var(--orange)}
.head-blog{left:264px;background:var(--orange)}
.head-tweet{left:470px;background:var(--sky)}
.news-item{left:64px;width:170px}
.news-item h3{font-size:9px;font-weight:400;color:#111}
.news-meta{font-size:7px;color:#555;margin:3px 0 9px}
.news-item p{font-size:6.8px;line-height:10.8px;color:var(--body)}
.details{display:block;font-size:6.8px;color:var(--red-link);margin-top:7px}
.blog-item{left:263px;width:180px;display:flex;gap:8px}
.blog-thumb{width:53px;height:44px;flex:none;border:1px solid #ccc;margin-top:1px}
.blog-item h3{font-size:8.6px;font-weight:400;color:#111;margin-bottom:2px}
.blog-item p{font-size:6.8px;line-height:10.6px;color:var(--body)}
.blog-item .more{font-size:6.8px;color:var(--red-link);display:block;margin-top:3px}
.follow{left:486px;top:705px;display:flex;gap:4px;font-size:6.3px}
.follow span{border:1px solid #bbb;border-radius:3px;padding:1px 5px;background:#f5f5f5}
.tweet{left:472px;width:175px;display:flex;gap:8px}
.avatar{width:30px;height:29px;flex:none}
.tweet p{font-size:6.8px;line-height:10.8px;color:#333}
.tweet b{font-weight:400;color:var(--link)}

/* call band */
.call-band{left:0;top:936px;width:711px;height:86px;background:linear-gradient(#ff9e1c,var(--orange-dark) 75%,#f4a43c)}
.call-art{left:150px;top:948px;width:80px;height:63px;border-radius:40% 40% 12px 12px;background:linear-gradient(135deg,#ffa236,#1a6fd4 55%,#0d3e86)}
.call-text{left:243px;top:944px;color:#fff;font-size:14.5px;line-height:21.5px}
.call-text .local{font-size:12.5px;color:#111}

/* footer */
.site-footer{left:0;top:1022px;width:711px;height:136px;background:var(--footer)}
.foot-col{top:1038px;color:#ddd}
.foot-col h4{font-size:9.5px;font-weight:400;margin-bottom:8px}
.foot-col li{list-style:none;font-size:6.6px;line-height:14.2px}
.links li::before{content:"›";margin-right:6px}
.connect{left:500px;top:1038px;width:140px}
.connect h4{font-size:9.5px;font-weight:400;color:#ddd;text-align:right;margin-bottom:9px}
.connect-grid{display:grid;grid-template-columns:1fr 1fr;row-gap:9px;column-gap:8px}
.connect-grid div{display:flex;justify-content:flex-end;align-items:center;gap:5px;font-size:6.8px;color:#ddd}
.connect-grid i{width:12px;height:12px;display:block}
.copyright{left:0;top:1158px;width:711px;height:42px;background:var(--footer-base);border-top:1px solid #444;color:#bbb;font-size:6.6px;text-align:center;line-height:34px}
</style>
</head>
<body>

<header class="abs site-header"></header>
<div class="abs brand">CORVANE NETWORKS</div>
<div class="abs hotline">
  <svg width="13" height="11" viewBox="0 0 13 11"><path d="M1 3C1 1 4 0.5 6.5 0.5S12 1 12 3L10 4 9 2.5H4L3 4Z" fill="#cfcfcf"/><rect x="2" y="5" width="9" height="5.5" rx="1" fill="#cfcfcf"/></svg>
  1-844-7NU-LINK
</div>
<div class="abs account">Register | Login</div>
<div class="abs social-dots"><span></span><span></span><span></span></div>

<nav class="abs main-nav">
  <a class="active">Home</a><a>Services Plans</a><a>Coverage Map</a><a>About Us</a>
</nav>

<div class="abs hero-band"></div>
<section class="abs slider">
  <div class="abs slider-photo" role="img" aria-label="Man on the phone working at a desktop computer in a bright office"></div>
  <div class="abs slider-arrow"></div>
  <h1 class="abs hero-title">WEST MICHIGAN'S BEST<br>INTERNET SERVICE</h1>
  <ul class="abs hero-points">
    <li>FASTER SPEED <svg width="15" height="12" viewBox="0 0 15 12"><path d="M1 6L5.5 10.5 14 1.5" fill="none" stroke="var(--orange)" stroke-width="3"/></svg></li>
    <li>NO LIMITS <svg width="15" height="12" viewBox="0 0 15 12"><path d="M1 6L5.5 10.5 14 1.5" fill="none" stroke="var(--orange)" stroke-width="3"/></svg></li>
    <li>MORE VALUE <svg width="15" height="12" viewBox="0 0 15 12"><path d="M1 6L5.5 10.5 14 1.5" fill="none" stroke="var(--orange)" stroke-width="3"/></svg></li>
  </ul>
</section>
<div class="abs hero-shadow"></div>

<h2 class="abs section-title services-title">Our <em>Services</em></h2>
<div class="abs service-card card-home">
  <div class="photo" role="img" aria-label="Woman using a laptop and phone at home"></div>
  <div class="caption">Residential Plans</div>
</div>
<div class="abs service-card card-business">
  <div class="photo" role="img" aria-label="Two smiling business people in an office"></div>
  <div class="caption">Business Plans</div>
</div>
<div class="abs service-card card-coverage">
  <div class="photo" role="img" aria-label="Map of Michigan coverage area"></div>
  <div class="abs address-field">Enter Your Address</div>
  <div class="caption">Am I covered?<span class="check-btn">CHECK NOW</span></div>
</div>

<h2 class="abs section-title welcome-title">WELCOME TO CORVANE <em>SPEED</em></h2>
<div class="abs rule"></div>
<p class="abs welcome-text">Pellentesque luctus diam nec sapien rutrum suscipit. Duis ac blandit est, a vulputate nulla. Donec non elit ullamcorper, laoreet nunc vitae, laoreet est. Cras vehicula porttitor ante, aliquet vestibulum arcu tempus in. Aenean imperdiet luctus metus, sit amet ultricies orci dictum eget. Morbi sagittis leo eget nisi euismod semper. Vestibulum pharetra velit ligula, nec sodales arcu tincidunt quis. Praesent elit nisi, euismod eget consectetur quis, tincidunt nec justo. Maecenas sit amet neque nisi. Donec fringilla lacinia orci, non mattis libero tincidunt id. Integer ultricies fermentum tincidunt. Nunc eu ligula sodales, pretium orci vel, iaculis elit. Vestibulum leo erat, feugiat eu fermentum sed, egestas non diam. Donec quis felis vel felis malesuada tempus eget id velit. In hac habitasse platea dictumst.</p>
<div class="abs more-btn">More</div>

<h2 class="abs col-head head-news">Latest News</h2>
<h2 class="abs col-head head-blog">Latest Blog Posts</h2>
<h2 class="abs col-head head-tweet">Latest Tweet</h2>

<article class="abs news-item" style="top:707px">
  <h3>Mauris lectus lectus, consequat feugiat.</h3>
  <div class="news-meta">◷ Jan 27, 2014 &nbsp;&nbsp;&nbsp; ● 12</div>
  <p>Sed rhoncus sapien egestas neque porta posuere. Ut tincidunt nibh id lorem imperdiet scelerisque. Donec interdum, ante et auctor tincidunt felis felis adipiscing nulla, a adipiscing diam......</p>
  <span class="details">Details &gt;&gt;</span>
</article>
<article class="abs news-item" style="top:814px">
  <h3>Mauris lectus lectus, consequat feugiat.</h3>
  <div class="news-meta">◷ Jan 27, 2014 &nbsp;&nbsp;&nbsp; ● 12</div>
  <p>Sed rhoncus sapien egestas neque porta posuere. Ut tincidunt nibh id lorem imperdiet scelerisque. Donec interdum, ante et auctor tincidunt felis felis adipiscing nulla, a adipiscing diam......</p>
  <span class="details">Details &gt;&gt;</span>
</article>

<article class="abs blog-item" style="top:711px">
  <div class="blog-thumb" role="img" aria-label="Two people working at laptops" style="background:linear-gradient(135deg,#e5ead8,#7fa35a)"></div>
  <div><h3>Mauris Consequat Feugiat.</h3><p>Sed rhoncus sapien egestas neque porta posuere. Ut tincidunt nibh id lorem imperdiet scelerisque.</p><span class="more">More &gt;&gt;</span></div>
</article>
<article class="abs blog-item" style="top:780px">
  <div class="blog-thumb" role="img" aria-label="Computer monitor close-up" style="background:linear-gradient(135deg,#e9e9e9,#8e9298)"></div>
  <div><h3>Mauris Consequat Feugiat.</h3><p>Sed rhoncus sapien egestas neque porta posuere. Ut tincidunt nibh id lorem imperdiet scelerisque.</p><span class="more">More &gt;&gt;</span></div>
</article>
<article class="abs blog-item" style="top:849px">
  <div class="blog-thumb" role="img" aria-label="Person at a desk in an office" style="background:linear-gradient(135deg,#d9c6a8,#6f6355)"></div>
  <div><h3>Mauris Consequat Feugiat.</h3><p>Sed rhoncus sapien egestas neque porta posuere. Ut tincidunt nibh id lorem imperdiet scelerisque.</p><span class="more">More &gt;&gt;</span></div>
</article>

<div class="abs follow"><span>Follow @corvanelink</span><span>1,316 followers</span></div>
<div class="abs tweet" style="top:729px"><div class="avatar" role="img" aria-label="User avatar" style="background:linear-gradient(#6f8fb8,#2c3a4e)"></div><p><b>@HollisVantner</b> Down stock market this morning. Nothing special, just a little down.<b>reply</b></p></div>
<div class="abs tweet" style="top:775px"><div class="avatar" role="img" aria-label="User avatar" style="background:linear-gradient(#d8b49a,#8a5a3c)"></div><p><b>@HollisVantner</b> Down stock market this morning. Nothing special, just a little down.<b>reply</b></p></div>
<div class="abs tweet" style="top:819px"><div class="avatar" role="img" aria-label="User avatar" style="background:linear-gradient(#cfa58a,#7b5846)"></div><p><b>@HollisVantner</b> Down stock market this morning. Nothing special, just a little down.<b>reply</b></p></div>
<div class="abs tweet" style="top:867px"><div class="avatar" role="img" aria-label="User avatar" style="background:linear-gradient(#e0bca2,#6b4430)"></div><p><b>@HollisVantner</b> Down stock market this morning. Nothing special, just a little down.<b>reply</b></p></div>

<section class="abs call-band"></section>
<div class="abs call-art" role="img" aria-label="Blue rotary telephone"></div>
<p class="abs call-text">Call today to place an order or reach customer support<br>844-7NU-LINK<br><span class="local">Local number 517-555-0148</span></p>

<footer class="abs site-footer"></footer>
<div class="abs foot-col links" style="left:58px"><h4>Links</h4><ul><li>Service Plans</li><li>Coverage Map</li><li>Whois Corvane</li><li>Company Blog</li><li>Customer Support</li><li>Account Management</li></ul></div>
<div class="abs foot-col" style="left:201px"><h4>Support Staff Hours</h4><ul><li>Weekdays 7am to 10pm</li><li>Weekends 8am to 5pm</li><li>Holiday scheduling varies</li></ul></div>
<div class="abs foot-col" style="left:362px"><h4>Address</h4><ul><li>Corvane Networks, LLC</li><li>1187 Marlow Avenue</li><li>Ridgeford, MI 49301</li></ul>
  <h4 style="margin-top:14px">Email</h4><ul><li>support@corvanelink.com</li></ul></div>
<div class="abs connect"><h4>Connect With Us</h4>
  <div class="connect-grid">
    <div>Gatherly <i style="background:#3b5fa0"></i></div><div>Workwire <i style="background:#1a86c0"></i></div>
    <div>Chirpline <i style="background:#4fc0e8"></i></div><div>Orbit +1 <i style="background:#d9412f"></i></div>
    <div>RSS <i style="background:#f7861d"></i></div><div>Clipwall <i style="background:#cc2127"></i></div>
  </div>
</div>
<div class="abs copyright">© 2014 corvanelink.com. All rights reserved</div>

</body>
</html>
```